We are the world's leading center for transgender surgery and have multiple locations.

We want a unique and dynamic business card that wows potential patients and referral sources (physicians, previous patients, etc). We are open to inventive designs, card shape, additional design on the back of the card, etc.

We are a surgical practice in a competitive environment and want to stand out as the leader in transgender surgery. We have multiple surgeons with unique talents who are impeccably trained with extensive experience. We are dedicated to our patients and their needs. We want the card to stand out and impress them. We want it to be suitable to all of the surgeons as well as our staff.

Our practice started as a small practice in San Francisco, CA and now has an additional location in Austin Texas (as well as another city to be announced later). Our practice has plastic surgeons, reconstructive urologists, general surgeons and gynecologists.

We continue to boast some of the lowest published phalloplasty complication rates in the world and our San Francisco microsurgeons that we have been working with for more than a year and a half have 0 microvascular take backs and 0 flap failures. Between our two centers in San Francisco, California and Austin, Texas, we perform 5-6 phalloplasties per week, making us one of the largest volume centers in the world.

Target Market(s)

Potential Transgender patients (all genders) and referring physicians

Industry/Entity Type

Surgeon

Contact Information for Business Card

Here is an example of one of our physicians:

Daniel R. Venko, MD
Gender-Affirming Reconstructive Surgery and Care
Diplomate, National Council of Renal Medicine with advanced fellowship training in pelvic reconstruction

812 Orchard Vale Rd
Suite 4
Larkfield, CA 94917

phone 415-738-2914
fax 415-592-8167

Font styles to use
Sans Serif

Requirements
Must have
• Must have a unique look, but tasteful.
Nice to have
• ?
Should not have
• ?

```html
<!DOCTYPE html>
<html lang="en">
<head>
<meta charset="utf-8">
<title>Alder Center – Business Card</title>
<link rel="stylesheet" href="https://fonts.googleapis.com/css2?family=Source+Sans+3:wght@400;600&display=swap">
<style>
  :root {
    --navy: #21336b;
    --magenta: #a11d6b;
    --paper: #ffffff;
    --backdrop: #d3d5d8;
    --faint-pink: #f5e8ef;
  }
  * { margin: 0; padding: 0; box-sizing: border-box; }
  html, body { width: 1200px; height: 800px; overflow: hidden; }
  body {
    background: var(--backdrop);
    font-family: "Source Sans 3", sans-serif;
    position: relative;
  }
  .card {
    position: absolute;
    width: 560px;
    height: 320px;
    box-shadow: 0 6px 18px rgba(0,0,0,0.18);
    overflow: hidden;
  }
  .card-back {
    left: 560px; top: 60px;
    background: var(--navy);
    display: flex; align-items: center; justify-content: center;
  }
  .brand {
    display: flex; align-items: center; gap: 14px;
    font-weight: 600;
    letter-spacing: 0.02em;
  }
  .brand-dot { border-radius: 50%; flex: none; }
  .card-back .brand { color: var(--paper); font-size: 40px; }
  .card-back .brand-dot { width: 46px; height: 46px; background: var(--magenta); }

  .card-front {
    left: 80px; top: 410px;
    background: var(--paper);
  }
  .front-decor {
    position: absolute; right: -60px; top: 40px;
    width: 220px; height: 220px; border-radius: 50%;
    background: var(--faint-pink);
    z-index: 0;
  }
  .card-front .brand {
    position: absolute; left: 34px; top: 28px;
    color: var(--navy); font-size: 28px;
    z-index: 1;
  }
  .card-front .brand-dot { width: 34px; height: 34px; background: var(--magenta); }
  .person { position: absolute; left: 34px; top: 102px; right: 34px; z-index: 1; }
  .person-name { color: var(--magenta); font-weight: 600; font-size: 21px; line-height: 1.15; margin-bottom: 2px; }
  .person-role { color: var(--navy); font-size: 14.5px; line-height: 1.3; }
  .rule {
    position: absolute; left: 34px; right: 40px; top: 200px;
    height: 1.5px; background: var(--magenta);
    z-index: 1;
  }
  .address {
    position: absolute; left: 34px; top: 214px;
    color: var(--navy); font-size: 15px; line-height: 1.3;
    font-style: normal;
    z-index: 1;
  }
  .contact {
    position: absolute; left: 290px; top: 214px;
    color: var(--navy); font-size: 15px; line-height: 1.3;
    list-style: none;
    z-index: 1;
  }
  .contact li { display: flex; align-items: center; gap: 7px; }
  .contact svg { width: 14px; height: 14px; fill: var(--magenta); flex: none; }
  .footer-band {
    position: absolute; left: 0; right: 0; bottom: 0; height: 22px;
    background: var(--navy);
    z-index: 1;
  }
  .footer-accent {
    position: absolute; left: 0; bottom: 0; width: 48px; height: 22px;
    background: var(--magenta);
    z-index: 2;
  }
</style>
</head>
<body>
  <section class="card card-back" aria-label="Card back">
    <div class="brand"><span class="brand-dot"></span><span>ALDER CENTER</span></div>
  </section>

  <section class="card card-front" aria-label="Card front">
    <div class="front-decor"></div>
    <div class="brand"><span class="brand-dot"></span><span>ALDER CENTER</span></div>

    <div class="person">
      <p class="person-name">Daniel R. Venko, MD</p>
      <p class="person-role">Gender-Affirming Reconstructive Surgery and Care</p>
      <p class="person-role">Diplomate, National Council of Renal Medicine</p>
      <p class="person-role">with advanced fellowship training in pelvic reconstruction</p>
    </div>

    <div class="rule"></div>

    <address class="address">
      812 Orchard Vale Rd<br>
      Suite 4, Larkfield, CA 94917
    </address>

    <ul class="contact">
      <li>
        <svg viewBox="0 0 24 24" aria-label="Phone"><path d="M6.6 10.8a15.1 15.1 0 0 0 6.6 6.6l2.2-2.2c.3-.3.7-.4 1-.2 1.1.4 2.3.6 3.6.6.6 0 1 .4 1 1V20c0 .6-.4 1-1 1A17 17 0 0 1 3 4c0-.6.4-1 1-1h3.5c.6 0 1 .4 1 1 0 1.3.2 2.5.6 3.6.1.3 0 .7-.2 1z"/></svg>
        415-738-2914
      </li>
      <li>
        <svg viewBox="0 0 24 24" aria-label="Fax"><path d="M7 2h8l3 3v5H7zM4 10h16a2 2 0 0 1 2 2v8a2 2 0 0 1-2 2H4a2 2 0 0 1-2-2v-8a2 2 0 0 1 2-2zm3 4v2h4v-2zm0 3v2h4v-2z"/></svg>
        415-592-8167
      </li>
    </ul>

    <div class="footer-band"></div>
    <div class="footer-accent"></div>
  </section>
</body>
</html>
```